Commercial Cleaning Company Needs A Flyer

We are a commercial cleaning company based in London.
We are currently trying to grow our client base and would like a fresh, professional flyer that differentiates us from the competition. We mainly specialises in commercial cleaning such as offices, educational facilities etc. I would like to see a flyer design that look professional, unique not cheap. I have attached a file that contains some company details but Im happy to explore other options if thay are relevant. Please also find company logo and colour chart, this should remain as is.

I have attached some pictures that contain diamond shaped windows. I feel that this can be used to represent and incorporate the logo. Please add to flyer where possible.

Please feel free to contact me for any further advice.
Thanks and good luck

Target Market(s)

commercial buildings and residential property owners

Industry/Entity Type

Cleaning Service

Contact Information for Business Card

Please refer to up loaded document for company details and logo colours.

Font styles to use
Sans Serif

Colors
33a6d7
33b8a4

Requirements
Must have
• Look Professional, not cheap, unique, stand out from others.

```html
<!DOCTYPE html>
<html lang="en">
<head>
<meta charset="utf-8">
<title>Brightwell Cleaning Services – Flyer</title>
<link href="https://fonts.googleapis.com/css2?family=Arimo:wght@400;700&display=swap" rel="stylesheet">
<style>
  :root{
    --brand-blue:#33a6d7;
    --brand-teal:#33b8a4;
    --blue-deep:#1f86c4;
    --blue-light:#4ec0ec;
    --ink:#1b1b1b;
    --charcoal:#2b2b2b;
    --white:#ffffff;
  }
  *{margin:0;padding:0;box-sizing:border-box}
  html,body{width:928px;height:1200px;overflow:hidden;background:var(--white)}
  body{font-family:"Arimo",Arial,sans-serif;color:var(--ink)}
  .flyer{position:relative;width:928px;height:1200px;overflow:hidden;background:var(--white)}

  /* Top band */
  .about{position:absolute;left:0;top:0;width:535px;height:560px;
    background:linear-gradient(160deg,var(--blue-light) 0%,var(--brand-blue) 45%,var(--blue-deep) 100%);
    color:var(--white);padding:66px 20px 0 47px;font-size:15.6px;line-height:1.28}
  .about__tab{position:absolute;left:0;top:24px;width:171px;height:31px;background:var(--white);
    color:var(--brand-blue);font-weight:700;font-size:18px;letter-spacing:.5px;padding:6px 0 0 49px}
  .about p{margin-bottom:10px}
  .about .pledge{font-size:17px;margin:22px 0 18px;line-height:1.33}
  .values{list-style:none;font-size:17px;line-height:1.3}
  .values b{font-weight:700}

  .photo{position:absolute;left:535px;width:393px}
  .photo--office{top:0;height:294px;
    background:linear-gradient(180deg,#e9ecef 0%,#cfd4d8 45%,#6d7278 75%,#3a3d42 100%)}
  .photo--skyline{top:294px;height:266px;
    background:linear-gradient(180deg,#c9cdd1 0%,#a9aeb3 45%,#6e6a66 75%,#3d3a38 100%)}

  /* Headline */
  .headline{position:absolute;left:0;top:572px;width:928px;text-align:center;
    font-size:43px;line-height:1.2;font-weight:400;color:var(--ink)}

  /* Columns */
  .col{position:absolute;top:700px}
  .col--commercial{left:45px}
  .col--green{left:306px}
  .col--residential{left:611px}
  .col h2{font-size:17.5px;font-weight:700;margin-bottom:9px;letter-spacing:.1px}
  .col h2 span{color:var(--brand-blue)}
  .checklist{list-style:none;font-size:17.5px;line-height:21.8px}
  .checklist li{display:flex;align-items:center;gap:6px}
  .tick{width:12px;height:12px;flex:none}

  /* Bottom */
  .services{position:absolute;left:0;top:892px;width:433px;height:308px;background:var(--charcoal);color:var(--white)}
  .services__notch{position:absolute;left:170px;top:877px;width:263px;height:15px;background:var(--white)}
  .services__tab{position:absolute;left:0;top:877px;width:170px;height:15px;background:var(--charcoal)}
  .services h2{position:absolute;left:48px;top:-12px;color:var(--brand-blue);font-size:17.5px;font-weight:700}
  .services .checklist{position:absolute;left:48px;top:30px;font-size:17.5px}

  .contact{position:absolute;left:433px;top:923px;width:495px;height:277px;background:var(--charcoal)}
  .contact__corner{position:absolute;left:433px;top:892px;width:0;height:0;
    border-left:33px solid var(--brand-teal);border-top:31px solid transparent}
  .brand{position:absolute;left:58px;top:56px;display:flex;align-items:center;gap:14px;color:var(--brand-teal)}
  .brand__mark{width:22px;height:22px;background:var(--brand-teal)}
  .brand__name{font-size:29px;letter-spacing:2.4px;font-weight:400}
  .brand__tagline{position:absolute;left:94px;top:98px;color:var(--brand-teal);font-size:20px;letter-spacing:2.2px}
  .contact__list{position:absolute;left:153px;top:130px;list-style:none;color:var(--brand-teal);font-size:16px;line-height:20px}
  .contact__list span{display:inline-block;width:54px}
</style>
</head>
<body>
<div class="flyer">
  <svg width="0" height="0" style="position:absolute">
    <symbol id="tick" viewBox="0 0 12 12"><path d="M1 6.5 L4.3 10 L11 1.5" fill="none" stroke="currentColor" stroke-width="2"/></symbol>
  </svg>

  <section class="about">
    <div class="about__tab">ABOUT US</div>
    <p>Brightwell Cleaning Services continual commitment and dedication to delivering a quality service has enabled us to build a solid foundation within the cleaning industry.</p>
    <p>Our principle and objectives are simple, provide our customers with an affordable quality service to suit their needs and always put our clients first.</p>
    <p>BCS rewards dependability, integrality and provide the training and development for all employees to achieve the best possible results. We believe that building relationships based on ethical conduct towards employees and clientele defines our unique working environments and is a vital key to our success.</p>
    <p class="pledge">This is why at Brightwell Cleaning Services stand behind<br>our performance and guarantee your satisfaction.</p>
    <ul class="values">
      <li><b>Q</b>uick response to costumers needs guaranteed</li>
      <li><b>U</b>nequal attention to detail</li>
      <li><b>A</b>ffordable cleaning tailored to your needs</li>
      <li><b>L</b>engthy industry experience</li>
      <li><b>I</b>nsurance inclusive of Workers Compensation and Liability</li>
      <li><b>T</b>raining provided to all staff and supervisors</li>
      <li><b>Y</b>our satisfaction is our priority</li>
    </ul>
  </section>
  <div class="photo photo--office" role="img" aria-label="Photo of a bright open-plan office behind diamond-framed glass windows"></div>
  <div class="photo photo--skyline" role="img" aria-label="Photo of a city skyline seen through diamond-shaped window frames"></div>

  <h1 class="headline">We aim to offer the highest Commercial<br>and Residential cleaning standards.</h1>

  <div class="col col--commercial">
    <h2><span>COMMERCIAL</span> CLEANING</h2>
    <ul class="checklist">
      <li><svg class="tick"><use href="#tick"/></svg>Offices</li>
      <li><svg class="tick"><use href="#tick"/></svg>Education Facilities</li>
      <li><svg class="tick"><use href="#tick"/></svg>Medical Facilities</li>
      <li><svg class="tick"><use href="#tick"/></svg>Restaurants</li>
      <li><svg class="tick"><use href="#tick"/></svg>Showroom</li>
    </ul>
  </div>
  <div class="col col--green">
    <h2><span>GREEN CLEANING</span> AVAILABLE</h2>
    <ul class="checklist">
      <li><svg class="tick"><use href="#tick"/></svg>No harmful chemicals</li>
      <li><svg class="tick"><use href="#tick"/></svg>safe for children and pets</li>
      <li><svg class="tick"><use href="#tick"/></svg>eco-friendly</li>
      <li><svg class="tick"><use href="#tick"/></svg>no artificial fragrances</li>
    </ul>
  </div>
  <div class="col col--residential">
    <h2><span>RESIDENTIAL</span> CLEANING</h2>
    <ul class="checklist">
      <li><svg class="tick"><use href="#tick"/></svg>House Cleaning</li>
      <li><svg class="tick"><use href="#tick"/></svg>Apartment Cleaning</li>
      <li><svg class="tick"><use href="#tick"/></svg>Move In/Out Cleaning</li>
      <li><svg class="tick"><use href="#tick"/></svg>After Event Cleaning</li>
      <li><svg class="tick"><use href="#tick"/></svg>Spring Cleaning</li>
      <li><svg class="tick"><use href="#tick"/></svg>Post Building Works Deep Clean</li>
    </ul>
  </div>

  <div class="services__tab"></div>
  <div class="services__notch"></div>
  <section class="services">
    <h2>SERVICES</h2>
    <ul class="checklist" style="color:var(--white)">
      <li><svg class="tick" style="color:var(--brand-blue)"><use href="#tick"/></svg>General Cleaning Requirements</li>
      <li><svg class="tick" style="color:var(--brand-blue)"><use href="#tick"/></svg>Consumables supply and replacement</li>
      <li><svg class="tick" style="color:var(--brand-blue)"><use href="#tick"/></svg>Washroom services</li>
      <li><svg class="tick" style="color:var(--brand-blue)"><use href="#tick"/></svg>Building maintenance</li>
      <li><svg class="tick" style="color:var(--brand-blue)"><use href="#tick"/></svg>Window cleaning</li>
      <li><svg class="tick" style="color:var(--brand-blue)"><use href="#tick"/></svg>Carpet care</li>
      <li><svg class="tick" style="color:var(--brand-blue)"><use href="#tick"/></svg>Floor maintenance</li>
      <li><svg class="tick" style="color:var(--brand-blue)"><use href="#tick"/></svg>Scrubbing machinery</li>
      <li><svg class="tick" style="color:var(--brand-blue)"><use href="#tick"/></svg>PAT Testing</li>
      <li><svg class="tick" style="color:var(--brand-blue)"><use href="#tick"/></svg>Waste removal</li>
      <li><svg class="tick" style="color:var(--brand-blue)"><use href="#tick"/></svg>Recycling Programs</li>
    </ul>
  </section>

  <div class="contact__corner"></div>
  <section class="contact">
    <div class="brand">
      <div class="brand__mark"></div>
      <div class="brand__name">BRIGHTWELL CLEANING</div>
    </div>
    <div class="brand__tagline">Helping your business shine</div>
    <ul class="contact__list">
      <li><span>Email:</span>hello@brightwellcleaning.co.uk</li>
      <li><span>Web:</span>brightwellcleaning.co.uk</li>
      <li><span>Mobile:</span>07700900482</li>
      <li><span>Office:</span>02079460315</li>
    </ul>
  </section>
</div>
</body>
</html>
```